Digital Marketing Agency Business Card Design Project

We are a boutique marketing agency that provides premium digital marketing services that invlude
- strategic marketing plans
- Plovex Clickreach advertising
- Search engine optimization
- Digital business analytics
- Digital merketing consulting
Business card must have a premium look that makes c clear statement. We provide digital marketing services for multiple languages.

Business card on the back side should have a slogan. Boutique digital marketing.

We always go the extra mile by every project so that clients gep premium solution and 100% satisfaction.

Please design a business card that is one of a kind..

Thank you.

Psd logo uploaded and brief updated.

Target Market(s)

Companies that need strategic online presence that is reached with boutique digital marketing services in all verticals.

Industry/Entity Type

Marketing

Font styles to use
Sans Serif

Requirements
Must have
• Premium and prestigious look.
Nice to have
• Design unique business card that fits with provided logo.
Logo should include:
Tel., E-mail, web address
Business title: one is CEO, second is COO.
Business address.

Try designing dark and light version, dark with the grey-silver from the logo and light just white background with some abstract curves in blue or green.
Should not have
• No old-style design and font
No need to list our services on the business card.

```html
<!DOCTYPE html>
<html lang="en">
<head>
<meta charset="utf-8">
<title>Veloran Business Card</title>
<link href="https://fonts.googleapis.com/css2?family=Lato:wght@300;400;700;900&display=swap" rel="stylesheet">
<style>
  :root {
    --page-bg: #e9e6e1;
    --card-white: #ffffff;
    --card-shade: #f1f2f3;
    --brand-blue: #18aee3;
    --brand-blue-deep: #0f95c9;
    --brand-green: #a8c83a;
    --ink-grey: #6b6e72;
    --ink-dark: #2d2f33;
    --logo-grey: #8a8d91;
  }
  * { margin: 0; padding: 0; box-sizing: border-box; }
  html, body { width: 1200px; height: 1023px; overflow: hidden; }
  body {
    background: var(--page-bg);
    font-family: "Lato", Arial, sans-serif;
    position: relative;
  }
  .card {
    position: absolute;
    width: 560px;
    height: 320px;
    border-radius: 18px;
    overflow: hidden;
    box-shadow: 0 10px 28px rgba(0,0,0,0.18);
  }
  /* Front */
  .card-front {
    left: 90px; top: 130px;
    background: linear-gradient(180deg, var(--card-white) 0%, var(--card-shade) 100%);
  }
  .brand {
    position: absolute; left: 48px; top: 70px;
    display: flex; align-items: center; gap: 14px;
  }
  .brand-dot {
    width: 34px; height: 34px; border-radius: 50%;
    background: var(--brand-blue);
  }
  .brand-name {
    font-weight: 300; font-size: 40px; letter-spacing: 4px;
    color: var(--logo-grey);
  }
  .rule {
    position: absolute; left: 48px; top: 134px;
    width: 360px; height: 2px; background: var(--brand-green);
  }
  .person { position: absolute; left: 96px; top: 176px; }
  .person-name { font-weight: 900; font-size: 22px; color: var(--brand-blue); }
  .person-title { font-weight: 400; font-size: 15px; color: var(--ink-dark); margin-top: 2px; margin-left: 56px; }
  .contacts {
    position: absolute; right: 40px; top: 56px;
    list-style: none;
  }
  .contacts li {
    display: flex; align-items: center; gap: 8px;
    font-size: 15px; color: var(--ink-dark); line-height: 26px;
  }
  .contacts svg { width: 13px; height: 13px; }
  .band-green {
    position: absolute; right: 0; bottom: 52px;
    width: 240px; height: 12px; background: var(--brand-green);
    clip-path: polygon(12px 0, 100% 0, 100% 100%, 0 100%);
  }
  .band-blue {
    position: absolute; left: 0; right: 0; bottom: 0; height: 52px;
    background: linear-gradient(90deg, var(--brand-blue) 0%, var(--brand-blue-deep) 100%);
    display: flex; align-items: center; padding-left: 40px;
  }
  .slogan { color: #fff; font-weight: 700; font-size: 20px; }
  /* Back */
  .card-back {
    left: 560px; top: 560px;
    background: linear-gradient(160deg, #22baf0 0%, var(--brand-blue) 55%, var(--brand-blue-deep) 100%);
    display: flex; align-items: center; justify-content: center;
  }
  .card-back .brand { position: static; }
  .card-back .brand-dot { background: #ffffff; }
  .card-back .brand-name { color: #ffffff; font-size: 46px; }
</style>
</head>
<body>
  <section class="card card-front" aria-label="Business card front">
    <div class="brand">
      <span class="brand-dot"></span>
      <span class="brand-name">VELORAN</span>
    </div>
    <div class="rule"></div>
    <div class="person">
      <div class="person-name">Mara Lindqvist</div>
      <div class="person-title">Director</div>
    </div>
    <ul class="contacts">
      <li>
        <svg viewBox="0 0 12 12"><rect x="2.5" y="0.5" width="7" height="11" rx="1.2" fill="none" stroke="#18aee3"/></svg>
        555 010 287
      </li>
      <li>
        <svg viewBox="0 0 12 12"><rect x="0.5" y="2" width="11" height="8" fill="#18aee3"/><path d="M0.5 2 L6 7 L11.5 2" fill="none" stroke="#fff"/></svg>
        mara@veloran.net
      </li>
      <li>
        <svg viewBox="0 0 12 12"><circle cx="6" cy="6" r="5.5" fill="#18aee3"/><path d="M0.5 6H11.5M6 0.5V11.5M2 3H10M2 9H10" stroke="#fff" stroke-width="0.7"/></svg>
        www.veloran.net
      </li>
    </ul>
    <div class="band-green"></div>
    <div class="band-blue"><span class="slogan">Boutique Digital Marketing</span></div>
  </section>

  <section class="card card-back" aria-label="Business card back">
    <div class="brand">
      <span class="brand-dot"></span>
      <span class="brand-name">VELORAN</span>
    </div>
  </section>
</body>
</html>
```